Land Buying Company Needs Letterhead for Direct Mail Marketing to Land Owners

We are looking for a professional letterhead that we will be including in our direct mail marketing. We will be sending this to land owners who may be interested in selling or purchasing land.

The letterhead needs to be editable. Headers and footers would look nice, but we are open. We would want it to include our address, website, phone, and email info. For right now the address to use for design purposes would the following:

Address: 415 Bramwell Avenue #600
Dallas, TX 75219
Website - www.quillridgeacres.example
Email - info@quillridgeacres.example
Phone - 866-402-ACRE

I have attached our logo zip file that we just had done on Pixel Guild. Let me know what questions you have, and thank you.

```html
<!DOCTYPE html>
<html lang="en">
<head>
<meta charset="UTF-8">
<title>Quill Ridge Acres Letterhead</title>
<link href="https://fonts.googleapis.com/css2?family=Montserrat:wght@600&family=Barlow:wght@400&display=swap" rel="stylesheet">
<style>
  :root {
    --brand-dark: #4b5e1f;
    --brand-light: #9bc53d;
    --page-border: #8a8a8a;
    --paper: #ffffff;
    --backdrop: #ffffff;
  }
  * { margin: 0; padding: 0; box-sizing: border-box; }
  html, body {
    width: 918px;
    height: 1200px;
    overflow: hidden;
    background: var(--backdrop);
  }
  .sheet {
    position: absolute;
    left: 87px;
    top: 76px;
    width: 744px;
    height: 1048px;
    background: var(--paper);
    border: 1px solid var(--page-border);
    overflow: hidden;
  }
  .brand {
    position: absolute;
    left: 36px;
    top: 34px;
    display: flex;
    align-items: center;
    gap: 18px;
  }
  .brand-dot {
    width: 76px;
    height: 76px;
    border-radius: 50%;
    background: var(--brand-dark);
    flex: none;
  }
  .brand-name {
    font-family: "Montserrat", sans-serif;
    font-weight: 600;
    color: var(--brand-dark);
    line-height: 1;
  }
  .brand-name .line-main {
    display: block;
    font-size: 33px;
    letter-spacing: 1px;
  }
  .brand-name .line-sub {
    display: block;
    font-size: 16px;
    letter-spacing: 9px;
    margin-top: 8px;
  }
  .divider {
    position: absolute;
    left: 408px;
    top: 34px;
    width: 1px;
    height: 74px;
    background: var(--brand-light);
  }
  .contact {
    position: absolute;
    left: 428px;
    top: 32px;
    list-style: none;
    font-family: "Barlow", sans-serif;
    font-size: 13.5px;
    color: var(--brand-dark);
  }
  .contact li {
    display: flex;
    align-items: center;
    height: 19px;
  }
  .contact svg {
    width: 11px;
    height: 11px;
    margin-right: 10px;
    flex: none;
  }
  .footer-band {
    position: absolute;
    left: 0;
    right: 0;
    bottom: 0;
    height: 92px;
    background: linear-gradient(to bottom, rgba(155,197,61,0) 0%, rgba(155,197,61,0.55) 45%, var(--brand-light) 100%);
  }
</style>
</head>
<body>
  <div class="sheet">
    <header class="brand">
      <span class="brand-dot"></span>
      <div class="brand-name">
        <span class="line-main">QUILL RIDGE</span>
        <span class="line-sub">ACRES</span>
      </div>
    </header>
    <span class="divider"></span>
    <ul class="contact">
      <li>
        <svg viewBox="0 0 12 12"><path d="M6 1a3.3 3.3 0 0 0-3.3 3.3C2.7 7 6 10 6 10s3.3-3 3.3-5.7A3.3 3.3 0 0 0 6 1zm0 4.6a1.3 1.3 0 1 1 0-2.6 1.3 1.3 0 0 1 0 2.6z" fill="var(--brand-dark)"/><rect x="2" y="10.5" width="8" height="1" fill="var(--brand-light)"/></svg>
        415 Bramwell Avenue #600, Dallas, TX 75219
      </li>
      <li>
        <svg viewBox="0 0 12 12"><circle cx="6" cy="6" r="5" fill="none" stroke="var(--brand-dark)" stroke-width="1"/><path d="M1 6h10M6 1c-2 2.5-2 7.5 0 10M6 1c2 2.5 2 7.5 0 10" fill="none" stroke="var(--brand-dark)" stroke-width="0.8"/></svg>
        www.quillridgeacres.example
      </li>
      <li>
        <svg viewBox="0 0 12 12"><rect x="1" y="3" width="10" height="7" fill="var(--brand-dark)"/><path d="M1 3l5 4 5-4" fill="none" stroke="#fff" stroke-width="0.8"/></svg>
        info@quillridgeacres.example
      </li>
      <li>
        <svg viewBox="0 0 12 12"><circle cx="6" cy="6" r="5" fill="none" stroke="var(--brand-dark)" stroke-width="0.9"/><path d="M4 3.3l1 1.2-.6.8c.4.9 1.1 1.6 2 2l.8-.6 1.2 1-.6 1c-2.2-.3-4.3-2.4-4.6-4.6z" fill="var(--brand-dark)"/></svg>
        866-402-ACRE
      </li>
    </ul>
    <div class="footer-band"></div>
  </div>
</body>
</html>
```